Brightwater Contracting-work at height professionals

Specializing In:
High Rise Window Washing
Interior atrium maintenance
Dryer vent cleaning
Building maintenance/inspection
Property maintenance
Pressure washing

Portray:experienced team, QUILN certified technicians,

Needs to portray the rope access industry and window washing via rope access (not bosun chair!)

Pictures are just examples only of our work

Designs are looking good! Check the brief again. I updated it

Please change “hi-rise to”High Rise” Thanks, and check rest of the brief for updates on spelling and wording Thanks, designs are looking good!

Aswell need a company logo with the designs Thanks

Target Market(s)

High rise property management companies

Industry/Entity Type

Property Maintenance

Contact Information for Business Card

Torvin Maddock
Brightwater Contracting
Work at height professionals
C:555-201-3387
E:torvin@brightwatercontracting.co
E:sales@brightwatercontracting.co
Serving southern Alberta

Font styles to use
Sans Serif

Colors

Requirements
Must have
• High Rise Window Washing
• Dryer Vent Cleaning
• Snow Management
• Interior Atriums Maintenance
• Property Maintenance
• QUILN Certified
Nice to have
• Work at Height Professionals
• For all your property maintenance needs
• A company logo
• Downtown Calgary Alberta background
Should not have
• Bosun chairs
• Hi-rise

```html
<!DOCTYPE html>
<html lang="en">
<head>
<meta charset="utf-8">
<title>Brightwater Contracting — Business Card</title>
<link rel="stylesheet" href="https://fonts.googleapis.com/css2?family=Exo+2:wght@500;700&family=Roboto:wght@400;700&display=swap">
<style>
  :root {
    --stage: #2a2a2a;
    --navy: #163a5c;
    --navy-deep: #0f2a44;
    --sky: #7ab6de;
    --paper: #ffffff;
    --ink: #1c3550;
    --rule: #8fb9d8;
  }
  * { box-sizing: border-box; margin: 0; padding: 0; }
  html, body { width: 1200px; height: 900px; overflow: hidden; }
  body {
    background: var(--stage);
    font-family: "Roboto", Arial, sans-serif;
    position: relative;
  }
  .card {
    position: absolute;
    left: 250px;
    width: 700px;
    height: 400px;
    overflow: hidden;
  }
  .card--front { top: 40px; background: var(--navy); color: var(--paper); }
  .card--back { top: 460px; background: var(--paper); color: var(--ink); }

  .skyline-photo {
    position: absolute; inset: 0;
    background: linear-gradient(180deg, #3f6f95 0%, #2a5679 45%, #1e4566 75%, #1f4a4a 100%);
    opacity: .9;
  }
  .brand {
    display: flex; align-items: center; gap: 12px;
    font-family: "Roboto", Arial, sans-serif;
    font-weight: 700; font-size: 30px; letter-spacing: .5px;
    text-transform: uppercase;
  }
  .brand__dot { width: 34px; height: 34px; border-radius: 50%; flex: none; }
  .card--front .brand { position: absolute; top: 44px; left: 0; right: 0; justify-content: center; color: var(--paper); }
  .card--front .brand__dot { background: var(--paper); }

  .services {
    position: absolute; top: 128px; left: 0; right: 0;
    list-style: none; text-align: center;
    font-size: 16px; line-height: 21px;
  }
  .services li::before {
    content: ""; display: inline-block; width: 7px; height: 7px; border-radius: 50%;
    background: var(--sky); margin-right: 9px; vertical-align: middle;
  }
  .front-rule { position: absolute; top: 312px; left: 50px; right: 50px; height: 1px; background: var(--rule); }
  .region {
    position: absolute; top: 330px; left: 0; right: 0; text-align: center;
    font-family: "Exo 2", Arial, sans-serif; font-weight: 500;
    font-size: 20px; letter-spacing: 1.5px; text-transform: uppercase;
  }

  .card--back .brand { position: absolute; top: 40px; left: 40px; color: var(--navy); font-size: 26px; }
  .card--back .brand__dot { background: var(--navy); width: 30px; height: 30px; }
  .contacts { position: absolute; top: 160px; left: 50px; list-style: none; font-size: 18px; line-height: 27px; }
  .contacts li { display: flex; align-items: center; gap: 10px; }
  .contacts svg { width: 18px; height: 18px; flex: none; }
  .tagline { position: absolute; top: 250px; left: 50px; font-size: 19px; line-height: 25px; }
  .tagline p + p { margin-top: 14px; }
  .holder {
    position: absolute; top: 185px; right: 55px;
    font-family: "Exo 2", Arial, sans-serif; font-weight: 700;
    font-size: 28px; letter-spacing: 1px; color: var(--sky); text-transform: uppercase;
  }
  .bands { position: absolute; left: 0; bottom: 0; width: 700px; height: 70px; }
</style>
</head>
<body>
  <section class="card card--front">
    <div class="skyline-photo" role="img" aria-label="Photo of a downtown city skyline with trees in the foreground, tinted blue"></div>
    <div class="brand"><span class="brand__dot"></span>Brightwater Contracting</div>
    <ul class="services">
      <li>High Rise Window Washing</li>
      <li>Interior atrium maintenance</li>
      <li>Dryer vent cleaning</li>
      <li>Building maintenance/inspection</li>
      <li>Property maintenance</li>
      <li>Snow management</li>
      <li>Experienced and reliable</li>
      <li>QUILN Certified</li>
    </ul>
    <div class="front-rule"></div>
    <p class="region">Serving Southern Alberta</p>
  </section>

  <section class="card card--back">
    <div class="brand"><span class="brand__dot"></span>Brightwater Contracting</div>
    <ul class="contacts">
      <li><svg viewBox="0 0 20 20" fill="none" stroke="#7ab6de" stroke-width="1.6"><path d="M5 3h3l1.5 4-2 1.5a10 10 0 0 0 4 4l1.5-2 4 1.5v3a2 2 0 0 1-2 2A14 14 0 0 1 3 5a2 2 0 0 1 2-2z"/></svg>555-201-3387</li>
      <li><svg viewBox="0 0 20 20" fill="none" stroke="#7ab6de" stroke-width="1.6"><rect x="2" y="4" width="16" height="12"/><path d="M2 4l8 7 8-7"/></svg>torvin@brightwatercontracting.co</li>
      <li><svg viewBox="0 0 20 20" fill="none" stroke="#7ab6de" stroke-width="1.6"><rect x="2" y="4" width="16" height="12"/><path d="M2 4l8 7 8-7"/></svg>sales@brightwatercontracting.co</li>
    </ul>
    <div class="tagline">
      <p>Work at height professionals</p>
      <p>Experienced team,<br>QUILN certified technicians</p>
    </div>
    <p class="holder">Torvin Maddock</p>
    <svg class="bands" viewBox="0 0 700 70" preserveAspectRatio="none" aria-hidden="true">
      <polygon points="0,32 470,32 450,44 0,44" fill="var(--navy-deep)"/>
      <polygon points="500,26 680,26 650,54 470,54" fill="var(--sky)"/>
    </svg>
  </section>
</body>
</html>
```